Redesign wellness clinic website

The project is redesign a wellness clinic http://www.thornleighvitality.example. The new website is to be responsive,clean,bright and a strong call to action which is to book an appointment. The logo will remain the same but the colour scheme on the website should be reflect purple white and green. I want it to be bright and cheerful and the feeling of clarity. The website shouldn't be overloaded with content but more visuals.

Target Market(s)

Anyone that has corporate wellness benefits within the downtown Toronto core. Majority of audience are professional working in Media, Telecommunications and Investments.

Industry/Entity Type

Health And Wellness

Number of Pages Required

5+ page

Font styles to use
Sans Serif

Colors
ffffff
886aae
acd036

Requirements
Must have
• -Strong call to action which is book an appointment like this page https://www.kestrelmotion.example/
• -Services provided icons on the page like https://www.brightpathvitalityhouse.example/
• - Pictures of a good visualizing a fit and healthy life
• - Strong ratings from Quorva, Zintrel, PostMaz, similar to this website http://www.summitbalancehealth.example/our-team-professionals/
• - Bright and clear
Should not have
• -No black and white images (redo our pictures)
• -Dark themes

```html
<!DOCTYPE html>
<html lang="en">
<head>
<meta charset="utf-8">
<title>Thornleigh Vitality Centre</title>
<link rel="stylesheet" href="https://fonts.googleapis.com/css2?family=Alegreya:wght@400;500;700&family=Open+Sans:ital,wght@0,400;0,600;0,700;1,400&display=swap">
<style>
:root{
  --purple:#7d2b85;
  --purple-dark:#6a2270;
  --green:#adbf31;
  --green-light:#c4d24f;
  --grey-bg:#efefef;
  --badge-fill:#e4e4e4;
  --award-fill:#f2a15f;
  --text:#555;
  --white:#fff;
  --serif:"Alegreya", Georgia, serif;
  --sans:"Open Sans", Arial, sans-serif;
}
*{margin:0;padding:0;box-sizing:border-box}
html,body{width:1200px;height:3191px;overflow:hidden}
body{position:relative;font-family:var(--sans);color:var(--text);background:var(--white)}
.abs{position:absolute}

/* header */
.hero{position:absolute;left:0;top:0;width:1200px;height:713px;background:linear-gradient(180deg,#cfe3f2 0%,#e5eef2 35%,#8fae5c 62%,#6f9440 100%)}
.hero-curve{position:absolute;left:0;top:560px}
.topbar{position:absolute;left:0;top:0;width:1200px;height:117px;background:var(--purple);border-bottom:3px solid var(--green)}
.logo-box{position:absolute;left:79px;top:0;width:236px;height:128px;background:var(--white);display:flex;flex-direction:column;align-items:center;justify-content:center;border-bottom:4px solid var(--purple);box-shadow:0 2px 6px rgba(0,0,0,.2)}
.logo-name{font-family:var(--serif);font-size:27px;color:var(--purple);line-height:1;font-weight:500}
.logo-tag{font-family:var(--serif);font-size:14px;color:var(--purple);margin-top:6px}
.phone{position:absolute;left:760px;top:22px;color:var(--white);font-size:20px;display:flex;align-items:center;gap:12px}
.social{position:absolute;top:17px;width:38px;height:38px;border-radius:50%;background:var(--purple-dark);border:1px solid rgba(255,255,255,.35)}
.nav{position:absolute;left:336px;top:71px;display:flex;gap:20px;font-size:17px;color:var(--white)}
.nav .active{color:var(--green-light)}

.hero-title{position:absolute;left:613px;top:205px;font-family:var(--serif);font-weight:700;font-size:64px;line-height:66px;color:var(--purple)}
.btn-book{position:absolute;left:613px;top:372px;width:249px;height:50px;border-radius:25px;background:var(--green);color:var(--white);font-family:var(--serif);font-size:20px;display:flex;align-items:center;justify-content:center;box-shadow:0 3px 5px rgba(0,0,0,.25)}

/* welcome */
.welcome-title{position:absolute;left:0;top:768px;width:1200px;text-align:center;font-family:var(--serif);font-weight:700;font-size:44px;color:var(--green)}
.welcome-title span{color:var(--purple)}
.welcome-text{position:absolute;left:170px;top:822px;width:860px;text-align:center;font-size:19px;line-height:30px;color:#666}

/* services */
.services{position:absolute;left:0;top:932px;width:1200px;height:717px;background:var(--grey-bg)}
.h2{font-family:var(--serif);font-weight:700;font-size:42px;color:var(--green)}
.h2 .p{color:var(--purple)}
.services .h2{position:absolute;left:0;top:34px;width:1200px;text-align:center}
.hub{position:absolute;left:398px;top:153px;width:404px;height:404px;border-radius:50%;background:#e2e2e2}
.hub-inner{position:absolute;left:50px;top:50px;width:304px;height:304px;border-radius:50%;background:#d2d2d2}
.hub-core{position:absolute;left:30px;top:30px;width:244px;height:244px;border-radius:50%;background:radial-gradient(circle at 40% 35%,#fff,#ececec 70%,#dcdcdc);box-shadow:0 8px 14px rgba(0,0,0,.3);display:flex;align-items:center;justify-content:center;font-family:var(--serif);font-size:34px;font-weight:700;color:var(--purple)}
.svc-icon{position:absolute;width:102px;height:102px;border-radius:50%;background:var(--white);border:3px solid var(--purple);display:flex;align-items:center;justify-content:center}
.svc-label{position:absolute;font-family:var(--serif);font-size:20px;font-weight:500;color:#333}

/* testimonials / blog */
.col-title{position:absolute;top:1690px}
.testi{position:absolute;left:79px;width:480px;display:flex;gap:20px}
.avatar{width:68px;height:68px;border-radius:50%;border:3px solid var(--purple);background:#e9d7c8;flex:none}
.testi p{font-style:italic;font-size:16px;line-height:27px;color:#666;margin-top:2px}
.testi .who{font-style:normal;font-size:16px;color:#444;margin-top:4px}
.post{position:absolute;left:638px;width:500px;display:flex;gap:18px}
.date{flex:none;width:60px;height:72px;display:flex;flex-direction:column}
.date .d{height:46px;background:var(--purple);color:var(--white);font-family:var(--serif);font-size:30px;font-weight:700;display:flex;align-items:center;justify-content:center}
.date .m{height:26px;background:#666;color:var(--white);font-size:15px;display:flex;align-items:center;justify-content:center}
.post h3{font-family:var(--serif);font-weight:500;font-size:19px;color:var(--purple);line-height:24px}
.post p{font-size:16px;line-height:26px;color:#666}

/* location band */
.band{position:absolute;left:0;top:2128px;width:1200px;height:209px;background:var(--green)}
.band-mark{position:absolute;left:79px;top:24px;width:166px;height:166px;border-radius:50%;border:4px solid var(--white);display:flex;align-items:center;justify-content:center;font-family:var(--serif);font-weight:700;font-size:26px;color:var(--white)}
.band h2{position:absolute;left:275px;top:52px;font-family:var(--serif);font-weight:700;font-size:42px;color:var(--white)}
.band p{position:absolute;left:275px;top:110px;font-size:16px;line-height:27px;color:var(--white)}
.btn-map{position:absolute;left:936px;top:81px;width:166px;height:46px;border-radius:23px;background:var(--white);color:var(--green);font-family:var(--serif);font-weight:700;font-size:19px;display:flex;align-items:center;justify-content:center}

/* ratings */
.badge{position:absolute;top:2462px;width:205px;height:134px;border:2px solid #c9c9c9;background:var(--white);display:flex;flex-direction:column;align-items:center;justify-content:center;gap:8px}
.badge .name{font-family:var(--sans);font-weight:700;font-size:36px;color:var(--purple)}
.badge small{font-size:14px;color:#666}
.badge .plain{width:150px;height:96px;border-radius:6px;background:var(--badge-fill)}

/* footer */
.footer{position:absolute;left:0;top:2640px;width:1200px;height:488px;background:var(--grey-bg)}
.foot-h{position:absolute;top:2822px;font-family:var(--serif);font-weight:700;font-size:22px;color:var(--green)}
.foot-text{position:absolute;font-size:15px;line-height:26px;color:#666}
.read-more{font-weight:700;color:var(--purple);text-decoration:underline;font-size:15px}
.tweet{position:absolute;left:347px;width:240px;display:flex;gap:12px;font-size:14px;line-height:22px;color:#777}
.tweet .ico{flex:none;width:16px;height:16px;border-radius:50%;background:var(--purple);margin-top:4px}
.tweet a{color:var(--purple)}
.video{position:absolute;left:615px;top:2862px;width:232px;height:138px;background:#111}
.award{position:absolute;left:889px;top:2862px;width:132px;height:140px;border-radius:6px;background:var(--award-fill)}
.award-text{position:absolute;left:889px;top:3010px;width:200px;font-size:14px;line-height:22px;color:#fafafa}
.copy{position:absolute;left:0;top:3128px;width:1200px;height:63px;background:var(--purple);color:var(--white);font-size:16px;display:flex;align-items:center;justify-content:center}
</style>
</head>
<body>

<div class="hero" role="img" aria-label="Photo of a smiling woman jogging on a park path lined with trees"></div>
<svg class="hero-curve" width="1200" height="160" viewBox="0 0 1200 160">
  <path d="M420 160 C700 120 980 60 1200 20 L1200 70 C1000 110 760 150 560 160 Z" fill="var(--purple)"/>
  <path d="M380 160 C650 110 950 50 1200 0 L1200 50 C980 100 720 150 520 160 Z" fill="var(--green)"/>
  <path d="M0 150 C150 110 300 95 480 110 C760 130 1000 75 1200 60 L1200 160 L0 160 Z" fill="var(--white)"/>
</svg>

<header class="topbar">
  <div class="phone">
    <svg width="18" height="18" viewBox="0 0 24 24"><path d="M6.6 10.8a15.1 15.1 0 0 0 6.6 6.6l2.2-2.2c.3-.3.7-.4 1-.2 1.1.4 2.3.6 3.6.6.6 0 1 .4 1 1V20c0 .6-.4 1-1 1A17 17 0 0 1 3 4c0-.6.4-1 1-1h3.5c.6 0 1 .4 1 1 0 1.3.2 2.5.6 3.6.1.3 0 .7-.2 1z" fill="#fff"/></svg>
    416-555-0142
  </div>
  <span class="social" style="left:943px" aria-label="Social link"></span>
  <span class="social" style="left:987px" aria-label="Social link"></span>
  <span class="social" style="left:1034px" aria-label="Social link"></span>
  <span class="social" style="left:1083px" aria-label="Social link"></span>
  <nav class="nav">
    <span class="active">Home</span><span>Fees and Services</span><span>Our Staff</span><span>News and Updates</span><span>Corporate Wellness</span><span>Forms</span><span>Contact</span>
  </nav>
</header>
<div class="logo-box">
  <div class="logo-name">Thornleigh Vitality</div>
  <div class="logo-tag">many disciplines, one philosophy</div>
</div>

<h1 class="hero-title">many disciplines,<br>one philosophy</h1>
<div class="btn-book">BOOK APPOINTMENT</div>

<h2 class="welcome-title">Welcome to <span>thornleigh vitality centre</span></h2>
<p class="welcome-text">Our Centre is committed to helping improve and extend the lives of as many people as possible in our community. Come and join our Family and start changing your life today.</p>

<section class="services">
  <h2 class="h2">Our <span class="p">Best Services</span></h2>
  <div class="hub"><div class="hub-inner"><div class="hub-core">Thornleigh</div></div></div>

  <div class="svc-icon" style="left:411px;top:117px"><svg width="44" height="44" viewBox="0 0 44 44" fill="none" stroke="var(--green)" stroke-width="3"><path d="M22 4v36M14 12h16M16 20c4 3 8 3 12 0M16 28c4 3 8 3 12 0"/></svg></div>
  <div class="svc-icon" style="left:685px;top:117px"><svg width="44" height="44" viewBox="0 0 44 44" fill="none" stroke="var(--green)" stroke-width="3"><circle cx="14" cy="16" r="4"/><path d="M6 28h32M10 34h24M20 22l12-6"/></svg></div>
  <div class="svc-icon" style="left:334px;top:262px"><svg width="44" height="44" viewBox="0 0 44 44" fill="none" stroke="var(--green)" stroke-width="3"><circle cx="26" cy="10" r="4"/><path d="M6 34h32M12 34V24h20v10M26 14v10"/></svg></div>
  <div class="svc-icon" style="left:762px;top:262px"><svg width="44" height="44" viewBox="0 0 44 44" fill="none" stroke="var(--green)" stroke-width="3"><path d="M16 6v20c0 6 4 10 10 10h8v-6h-8c-2 0-4-2-4-4V6"/></svg></div>
  <div class="svc-icon" style="left:383px;top:426px"><svg width="44" height="44" viewBox="0 0 44 44" fill="none" stroke="var(--green)" stroke-width="3"><circle cx="18" cy="7" r="3"/><path d="M18 12v12h10l4 10M14 18a10 10 0 1 0 12 14"/></svg></div>
  <div class="svc-icon" style="left:715px;top:426px"><svg width="44" height="44" viewBox="0 0 44 44" fill="none" stroke="var(--green)" stroke-width="3"><path d="M10 36l24-28M12 28h6M16 22h6M20 16h6M24 10h6"/></svg></div>
  <div class="svc-icon" style="left:549px;top:502px"><svg width="48" height="44" viewBox="0 0 48 44" fill="none" stroke="var(--green)" stroke-width="3"><path d="M24 38L8 22a9 9 0 0 1 16-12 9 9 0 0 1 16 12z"/><path d="M6 22h10l4-6 5 12 4-6h13"/></svg></div>

  <span class="svc-label" style="left:277px;top:143px">Chiropractic</span>
  <span class="svc-label" style="left:819px;top:143px">Massage Therapy</span>
  <span class="svc-label" style="left:178px;top:299px">Physiotherapy</span>
  <span class="svc-label" style="left:894px;top:299px">Chiropody</span>
  <span class="svc-label" style="left:170px;top:467px">Active Rehabilitation</span>
  <span class="svc-label" style="left:843px;top:467px">Osteopathy</span>
  <span class="svc-label" style="left:450px;top:620px;width:300px;text-align:center;line-height:30px">Nutrition and Lifestyle<br>Medicine</span>
</section>

<h2 class="h2 col-title" style="left:79px;color:var(--purple)">Client <span style="color:var(--green)">Testimonials</span></h2>
<div class="testi" style="top:1760px"><div class="avatar" role="img" aria-label="Client portrait"></div><div><p>Lorem Ipsum is simply dummy text of the printing and typesetting industry.</p><p class="who">- Client Name</p></div></div>
<div class="testi" style="top:1875px"><div class="avatar" role="img" aria-label="Client portrait"></div><div><p>Lorem Ipsum is simply dummy text of the printing and typesetting industry.</p><p class="who">- Client Name</p></div></div>
<div class="testi" style="top:1983px"><div class="avatar" role="img" aria-label="Client portrait"></div><div><p>Lorem Ipsum is simply dummy text of the printing and typesetting industry.</p><p class="who">- Client Name</p></div></div>

<h2 class="h2 col-title" style="left:638px;color:var(--purple)">Latest <span style="color:var(--green)">Blog</span></h2>
<div class="post" style="top:1762px"><div class="date"><span class="d">21</span><span class="m">mar</span></div><div><h3>Lorem Ipsum is simply dummy.</h3><p>Lorem Ipsum is simply dummy text of the printing and typesetting industry. Lorem Ipsum has been.</p></div></div>
<div class="post" style="top:1873px"><div class="date"><span class="d">21</span><span class="m">mar</span></div><div><h3>Lorem Ipsum is simply dummy.</h3><p>Lorem Ipsum is simply dummy text of the printing and typesetting industry. Lorem Ipsum has been.</p></div></div>
<div class="post" style="top:1977px"><div class="date"><span class="d">21</span><span class="m">mar</span></div><div><h3>Lorem Ipsum is simply dummy.</h3><p>Lorem Ipsum is simply dummy text of the printing and typesetting industry. Lorem Ipsum has been.</p></div></div>

<section class="band">
  <div class="band-mark">Thornleigh</div>
  <h2>Visit our new location</h2>
  <p>We are open for business at 7:30 am. Open 7 days a week!<br>Ask one of our associates about our Referral Reward Program!</p>
  <div class="btn-map">SEE MAP</div>
</section>

<h2 class="h2 abs" style="left:121px;top:2388px">Strong <span class="p">Ratings From</span></h2>
<h2 class="h2 abs" style="left:877px;top:2388px">Our <span class="p">Partner</span></h2>
<div class="badge" style="left:121px">
  <span class="name">Zintrel</span>
  <small>Great Reviews on Zintrel!</small>
</div>
<div class="badge" style="left:366px">
  <span class="name">Quorva</span>
  <small>5 Star Rating on Quorva</small>
</div>
<div class="badge" style="left:611px" role="img" aria-label="Top rated clinic listing badge">
  <div class="plain"></div>
</div>
<div class="badge" style="left:877px;width:208px">
  <span class="name">Marrow</span>
  <small>Dental Centres</small>
</div>

<div class="footer"></div>
<svg class="abs" style="left:0;top:2600px" width="1200" height="140" viewBox="0 0 1200 140">
  <path d="M0 0 H1200 V30 C1000 110 700 140 430 120 C260 106 120 70 0 60 Z" fill="var(--white)"/>
  <path d="M420 110 C700 130 980 90 1200 20 L1200 60 C980 130 700 150 420 110 Z" fill="var(--purple)"/>
</svg>

<h3 class="foot-h" style="left:79px">About us</h3>
<p class="foot-text" style="left:79px;top:2858px;width:210px">Established in 1989 the Thornleigh Vitality Centre has become one of Canada's leaders in providing quality care and innovative wellness programs for the community...<br><span class="read-more">READ MORE</span></p>

<h3 class="foot-h" style="left:347px">Our Tweets</h3>
<div class="tweet" style="top:2858px"><span class="ico"></span><div>@thornleighvital<br><a>tv.example/8qw68D5</a><br><span style="color:var(--purple)">♡ ↪</span> <span style="float:right">4 days ago</span></div></div>
<div class="tweet" style="top:2940px"><span class="ico"></span><div>@thornleighvital<br><a>tv.example/8qw68D5</a><br><span style="color:var(--purple)">♡ ↪</span> <span style="float:right">4 days ago</span></div></div>

<h3 class="foot-h" style="left:615px">Video Review</h3>
<div class="video">
  <svg width="232" height="138" viewBox="0 0 232 138">
    <circle cx="116" cy="50" r="22" fill="#333"/><path d="M109 39v22l18-11z" fill="#ddd"/>
    <path d="M14 112v14l11-7z" fill="#fff"/>
    <rect x="34" y="118" width="30" height="2" fill="#888"/><circle cx="36" cy="119" r="4" fill="#fff"/>
    <text x="120" y="124" fill="#fff" font-family="Open Sans, sans-serif" font-size="12">0:00</text>
    <rect x="170" y="114" width="10" height="10" fill="#fff"/><rect x="196" y="112" width="14" height="14" fill="none" stroke="#fff" stroke-width="2"/>
  </svg>
</div>
<span class="abs" style="left:615px;top:3020px;width:30px;height:30px;background:#555"></span>
<span class="abs" style="left:655px;top:3020px;width:30px;height:30px;background:#5ab4e6"></span>

<h3 class="foot-h" style="left:883px">Award</h3>
<div class="award" role="img" aria-label="Community choice award badge"></div>
<p class="award-text">Thornleigh Vitality Centre is voted a leading Wellness Centre in the community</p>

<footer class="copy">©thornleigh vitality centre. 2017 - All Rights Reserved.</footer>

</body>
</html>
```